I will ask the design of the business card

We are looking for business card design of the new company "TORVIK QUANTA WORKS LLC." Based in Azerbaijan.
In case
We are working on Azerbaijan to set up the first exchange of crypto currencies.

The key currency used in exchanges is called "MELDA".
In case
We are doing project to make crypto currency infrastructure.

We provide state-of-the-art technology to the world.

```html
<!DOCTYPE html>
<html lang="en">
<head>
<meta charset="utf-8">
<title>Torvik Quanta Works LLC — Business Card</title>
<link rel="stylesheet" href="https://fonts.googleapis.com/css2?family=Open+Sans:wght@400;600;700&display=swap">
<style>
  :root {
    --backdrop: #595959;
    --card-light: #f3f3f3;
    --card-navy: #100b46;
    --ink-navy: #100b46;
    --ink-body: #1f1f1f;
    --ink-white: #ffffff;
  }
  * { margin: 0; padding: 0; box-sizing: border-box; }
  html, body {
    width: 1200px;
    height: 900px;
    overflow: hidden;
  }
  body {
    position: relative;
    background: var(--backdrop);
    font-family: "Open Sans", Arial, sans-serif;
  }
  .card {
    position: absolute;
    top: 200px;
    width: 310px;
    height: 502px;
  }
  .card--front {
    left: 253px;
    background: var(--card-light);
    border-radius: 62px 0 62px 0;
  }
  .card--back {
    left: 627px;
    background: var(--card-navy);
    border-radius: 0 62px 0 62px;
  }
  .wordmark {
    position: absolute;
    left: 0;
    width: 100%;
    text-align: center;
    font-weight: 600;
    font-size: 24px;
    line-height: 30px;
    letter-spacing: 0.5px;
  }
  .card--front .wordmark { top: 140px; color: var(--ink-navy); }
  .card--back .wordmark { top: 220px; color: var(--ink-white); }

  .contact {
    position: absolute;
    left: 33px;
    top: 293px;
    color: var(--ink-body);
  }
  .contact__name {
    font-weight: 700;
    font-size: 18px;
    line-height: 22px;
    color: var(--ink-navy);
    letter-spacing: 0.3px;
  }
  .contact__role {
    font-size: 14px;
    line-height: 18px;
    margin-bottom: 10px;
  }
  .contact__list { list-style: none; }
  .contact__item {
    display: flex;
    align-items: center;
    font-size: 14px;
    line-height: 18px;
  }
  .contact__icon {
    width: 12px;
    height: 12px;
    margin-right: 6px;
    fill: var(--ink-navy);
    flex: none;
  }
  .contact__address {
    font-size: 14px;
    line-height: 18px;
    margin-top: 8px;
  }
</style>
</head>
<body>
  <section class="card card--front" aria-label="Card front">
    <div class="wordmark">TORVIK QUANTA<br>WORKS LLC.</div>
    <div class="contact">
      <p class="contact__name">ELNUR KAMALOV</p>
      <p class="contact__role">Managing Director</p>
      <ul class="contact__list">
        <li class="contact__item">
          <svg class="contact__icon" viewBox="0 0 12 12" aria-hidden="true"><path d="M1 4.5C1 2.5 3 2 6 2s5 .5 5 2.5v.8H8.6v-1H3.4v1H1z"/><path d="M3 6h6l1.2 4H1.8z"/></svg>
          012-480 336 215
        </li>
        <li class="contact__item">
          <svg class="contact__icon" viewBox="0 0 12 12" aria-hidden="true"><path d="M3.5 0.5h5a1 1 0 0 1 1 1v9a1 1 0 0 1-1 1h-5a1 1 0 0 1-1-1v-9a1 1 0 0 1 1-1zM4 2v7h4V2zM6 9.6a.6.6 0 1 0 0 1.2.6.6 0 0 0 0-1.2z" fill-rule="evenodd"/></svg>
          012-480 336 215
        </li>
        <li class="contact__item">
          <svg class="contact__icon" viewBox="0 0 12 12" aria-hidden="true"><path d="M1 2.5h10v1L6 6.8 1 3.5z"/><path d="M1 4.6l5 3.3 5-3.3V9.5H1z"/></svg>
          info@torvikquanta.az
        </li>
        <li class="contact__item">
          <svg class="contact__icon" viewBox="0 0 12 12" aria-hidden="true"><circle cx="6" cy="6" r="5"/><path d="M3 4.5c1-.3 1.6.4 1.2 1.2-.5.8.4 1.3 1 1.8.5.5 0 1.5.6 1.8" stroke="#f3f3f3" stroke-width="1" fill="none"/><path d="M7.2 2.2c.3.8 1.3.8 1.6 1.6" stroke="#f3f3f3" stroke-width="1" fill="none"/></svg>
          www.torvikquanta.az
        </li>
      </ul>
      <p class="contact__address">27 Nizami Street, Suite 4<br>Baku, Azerbaijan, AZ1000.</p>
    </div>
  </section>

  <section class="card card--back" aria-label="Card back">
    <div class="wordmark">TORVIK QUANTA<br>WORKS LLC.</div>
  </section>
</body>
</html>
```